MS Word Template needed for a company specialized in network and security infrastructures

We need a new MS Word Template. <br/>Our activity is services in IT (network infrastructure and security). We usually use french language. <br/>The template must be nice and beautiful, and easy to use. If possible, try to use as less as possible text zones to simplify redaction tasks. And try to use "native" polices in MS Word. I attached sample documents for example. Please try to use the same colour codes.

Target Market(s)

Consulting in Network and security domain

Industry/Entity Type

It Service

Colors

Designer to choose colors to be used in the design.

Requirements
Must have
• - Nice design
• - Easy to use
• - very professional aspect
Nice to have
• - actual oxa cable partners logo
• - actual colour code

```html
<!DOCTYPE html>
<html lang="fr">
<head>
<meta charset="utf-8">
<title>Oxa Cable Partners – Modèle de document</title>
<link rel="stylesheet" href="https://fonts.googleapis.com/css2?family=Montserrat:wght@500;600;700&family=Carlito:wght@400;700&display=swap">
<style>
  :root {
    --backdrop: #d6d6d6;
    --paper: #ffffff;
    --teal: #2f9ca0;
    --teal-deep: #2a8f99;
    --teal-light: #4fb3a8;
    --green: #3c9a6a;
    --green-soft: #5fae83;
    --lilac: #8f9fd6;
    --ink: #1f1f1f;
    --ink-soft: #444;
    --faint: #eef0f4;
  }
  * { margin: 0; padding: 0; box-sizing: border-box; }
  html, body { width: 1200px; height: 541px; overflow: hidden; background: var(--backdrop); }
  .canvas { position: relative; width: 1200px; height: 541px; }
  .page { position: absolute; top: 40px; background: var(--paper); overflow: hidden; }

  /* Cover page */
  .cover { left: 40px; width: 341px; height: 473px; }
  .cover-photo {
    position: absolute; left: 0; top: 0; width: 100%; height: 280px;
    background: linear-gradient(160deg, #3f8f6e 0%, #5aa586 45%, #2f8a7a 100%);
  }
  .cover-panel {
    position: absolute; left: 0; top: 280px; width: 100%; height: 180px;
    background: linear-gradient(180deg, #48ab9c 0%, #2c9fac 100%);
    color: var(--paper); text-align: center;
  }
  .cover-title {
    font-family: "Montserrat", sans-serif; font-weight: 700;
    font-size: 22px; line-height: 28px; margin-top: 36px; letter-spacing: 0.3px;
  }
  .cover-brand {
    display: flex; align-items: center; justify-content: center; gap: 8px;
    margin-top: 28px; font-family: "Montserrat", sans-serif; font-weight: 600; font-size: 14px;
  }
  .brand-dot { width: 22px; height: 22px; border-radius: 50%; background: currentColor; }
  .cover-strip { position: absolute; left: 0; bottom: 0; width: 100%; height: 13px; background: var(--green); }

  /* Divider page */
  .divider { left: 445px; width: 332px; height: 470px; }
  .divider svg { position: absolute; inset: 0; }
  .divider-brand {
    position: absolute; right: 26px; bottom: 42px;
    display: flex; align-items: center; gap: 8px;
    font-family: "Montserrat", sans-serif; font-weight: 600; font-size: 14px; color: var(--teal);
  }
  .divider-brand .brand-dot { width: 30px; height: 30px; }

  /* Table of contents page */
  .toc { left: 838px; width: 332px; height: 471px; font-family: "Carlito", sans-serif; color: var(--ink); }
  .toc-heading {
    position: absolute; left: 36px; right: 28px; top: 26px;
    text-align: center; font-size: 13px; letter-spacing: 0.3px;
    padding-bottom: 4px; border-bottom: 1px solid var(--ink-soft);
  }
  .toc-label { position: absolute; left: 38px; top: 67px; font-size: 10px; font-weight: 700; color: var(--teal-deep); }
  .toc-list { position: absolute; left: 38px; right: 33px; top: 88px; list-style: none; font-size: 6.4px; }
  .toc-list li { display: flex; align-items: baseline; height: 11px; }
  .toc-list .lead { flex: 1; border-bottom: 1px dotted #777; margin: 0 4px; transform: translateY(-1px); }
  .toc-list .minor { font-weight: 400; }
  .toc-list .major { font-weight: 700; }
  .toc-ornament {
    position: absolute; right: 0; bottom: 26px; width: 100px; height: 110px;
    background: linear-gradient(135deg, rgba(238,240,244,0) 0%, var(--faint) 60%);
  }
  .toc-footer { position: absolute; left: 0; right: 0; bottom: 7px; height: 16px; }
  .toc-footer svg { position: absolute; left: 0; top: 0; }
  .toc-url {
    position: absolute; left: 10px; top: 2px; font-size: 9px; font-weight: 700; color: var(--paper);
  }
  .toc-pageno { position: absolute; right: 16px; top: 3px; font-size: 7px; color: var(--ink); }
</style>
</head>
<body>
<main class="canvas">

  <section class="page cover">
    <div class="cover-photo" role="img" aria-label="Photo of a hand touching a digital network interface with nodes and a globe, in green tones"></div>
    <div class="cover-panel">
      <h1 class="cover-title">PRÉSENTATION<br>Oxa Cable Partners</h1>
      <div class="cover-brand"><span class="brand-dot"></span>Oxa Cable Partners</div>
    </div>
    <div class="cover-strip"></div>
  </section>

  <section class="page divider">
    <svg width="332" height="470" viewBox="0 0 332 470" aria-hidden="true">
      <rect width="332" height="470" fill="var(--paper)"/>
      <rect width="332" height="360" fill="var(--teal)"/>
      <polygon points="0,362 332,255 332,314 0,382" fill="var(--green)"/>
      <polygon points="0,382 332,314 332,318 0,385" fill="var(--lilac)"/>
      <polygon points="0,385 332,318 332,470 0,470" fill="var(--paper)"/>
    </svg>
    <div class="divider-brand"><span class="brand-dot"></span>Oxa Cable Partners</div>
  </section>

  <section class="page toc">
    <h2 class="toc-heading">TABLE OF CONTENTS</h2>
    <p class="toc-label">Contents</p>
    <ul class="toc-list">
      <li class="minor">Table of Contents<span class="lead"></span>01</li>
      <li class="major">Executive Summary<span class="lead"></span>02</li>
      <li class="major">Our Understanding of Your Needs<span class="lead"></span>02</li>
      <li class="major">Our Recommendations<span class="lead"></span>03</li>
      <li class="major">Our Approach<span class="lead"></span>05</li>
      <li class="major">Budget and Timeframe<span class="lead"></span>07</li>
      <li class="major">Appendix A: About Harlow Creek<span class="lead"></span>10</li>
      <li class="major">Appendix B: Selected Client List<span class="lead"></span>10</li>
      <li class="major">Appendix C: Our Capabilities<span class="lead"></span>11</li>
      <li class="major">Appendix D: Our Process<span class="lead"></span>12</li>
    </ul>
    <div class="toc-ornament" role="img" aria-label="Faint geometric chevron decoration"></div>
    <footer class="toc-footer">
      <svg width="332" height="16" viewBox="0 0 332 16" aria-hidden="true">
        <polygon points="0,0 196,0 212,16 0,16" fill="var(--teal)"/>
        <polygon points="199,0 205,0 221,16 215,16" fill="var(--teal-light)"/>
      </svg>
      <span class="toc-url">www.oxacable.net</span>
      <span class="toc-pageno">1</span>
    </footer>
  </section>

</main>
</body>
</html>
```